For our annual dance recital this year we will have an asylum/ orphans/ any spooky shelter. Thats the feel of it.
i will be need an invitation and a ticket.
as the recital will be done in two days the tickets will have same design but different colors.
My idea is to have spooky fonts/ x ray images somehow put in the design.
i will be uploading a lot of images for you to understand where i would like to take this design.
for the invitation i do want to have part of the paper printed in see through material like some of the images uploaded or have an x-ray effect.
the invitation should have this written on it.
DUSKMORE
Our production is ready and we are dying to have you around. So crawl on over for a spooktacular happening at
QASR MIRWAN UNIVERSITY AUDITORIUM
The undertaking will begin from 1:30pm to 3:30pm
May 2nd 2014 and May 3rd 2014
The entry tickets will be two colors but same design. i would like it to be printed of see through plastic paper. so we can have one see through and font in black and the other one is dark see through written in white maybe. please make in an xray effext with maybe the pointed feet picture somehow incorporated in the design
i want it to look like the picture i uploaded of (Wendels 4th birthday) in regard of layout of the writings i like how the date is stamped and i like how the date is pointed out in a dot.
here what to write on tickets
The name of the recital
Issued by Pavrella
DUSKMORE
(Find me a sentence that means admit one)
we do need numbers as the seats are numbered
so all in all i would like the invitation and ticket to go together i was thinking of having the dancer bridge xray on invitation and the pointed feet on the ticket.
if you have any other nice parts of the body xray that somehow show its a dancer im also open to that.
than main idea is to have a nice design that is so creative yet simple. play with the fonts to deliver this spooky feeling but all with elegance.
please notice that the picture with the person smoking Xray .. i like how its black and the words are see through with the xray picture. so this would be nice as an idea.
Reason: I still did not find a design that i like.
the theme is asylum. i want it creepy but in the same time ELEGANT. I will be printing invitation on CLEAR paper so the X ray picture could be incorporated in the design in a very subtle way.
Please ask me any question if its not clear
PS my budget is higher now.

```html
<!DOCTYPE html>
<html lang="en">
<head>
<meta charset="utf-8">
<title>Duskmore – Invitation</title>
<link href="https://fonts.googleapis.com/css2?family=Metal+Mania&family=Pathway+Gothic+One&family=Special+Elite&display=swap" rel="stylesheet">
<style>
  :root {
    --backdrop: #b5a07c;
    --card: #050505;
    --gold: #dcc79c;
    --gold-soft: #cdb68a;
    --bone-light: #b9b0aa;
    --bone-mid: #6e6764;
    --bone-dark: #1a1818;
  }
  * { margin: 0; padding: 0; box-sizing: border-box; }
  html, body {
    width: 1200px;
    height: 935px;
    overflow: hidden;
    background: var(--backdrop);
  }
  .stage {
    position: relative;
    width: 1200px;
    height: 935px;
  }
  .invitation {
    position: absolute;
    left: 80px;
    top: 186px;
    width: 1040px;
    height: 562px;
    background: var(--card);
    overflow: hidden;
    box-shadow: 0 6px 18px rgba(0, 0, 0, 0.35);
  }
  .xray-feet {
    position: absolute;
    right: 0;
    top: 0;
    width: 500px;
    height: 100%;
    background:
      radial-gradient(ellipse 90px 230px at 150px 250px, var(--bone-light), var(--bone-mid) 55%, transparent 80%),
      radial-gradient(ellipse 90px 230px at 330px 230px, var(--bone-light), var(--bone-mid) 55%, transparent 80%),
      radial-gradient(ellipse 200px 14px at 260px 480px, rgba(200, 200, 200, 0.45), transparent 80%),
      linear-gradient(90deg, var(--card), var(--bone-dark) 30%, var(--bone-dark) 80%, var(--card));
  }
  .text-block {
    position: absolute;
    left: 70px;
    top: 150px;
    width: 470px;
    color: var(--gold);
    text-align: center;
  }
  .title {
    font-family: "Metal Mania", cursive;
    font-weight: 400;
    font-size: 108px;
    line-height: 1;
    letter-spacing: 2px;
    text-align: left;
    margin-left: 10px;
  }
  .intro {
    font-family: "Pathway Gothic One", sans-serif;
    font-size: 26px;
    line-height: 1.25;
    margin-top: 14px;
    color: var(--gold-soft);
  }
  .venue {
    font-family: "Special Elite", cursive;
    font-size: 24px;
    letter-spacing: 0.5px;
    margin-top: 32px;
    white-space: nowrap;
  }
  .schedule {
    font-family: "Special Elite", cursive;
    font-size: 20px;
    line-height: 1.35;
    margin-top: 26px;
    color: var(--gold-soft);
  }
  .schedule .dates { font-size: 22px; }
  sup { font-size: 0.6em; }
</style>
</head>
<body>
<main class="stage">
  <section class="invitation">
    <div class="xray-feet" role="img" aria-label="X-ray of a dancer's two feet standing en pointe"></div>
    <div class="text-block">
      <h1 class="title">DUSKMORE</h1>
      <p class="intro">Our production is ready and we are dying<br>to have you around. So crawl on over<br>for a spooktacular happening at</p>
      <p class="venue">QASR MIRWAN UNIVERSITY AUDITORIUM</p>
      <p class="schedule">The undertaking will begin<br>from 1:30pm to 3:30pm<br><span class="dates">May 2<sup>nd</sup> 2014 and May 3<sup>rd</sup> 2014</span></p>
    </div>
  </section>
</main>
</body>
</html>
```